Business Card Design Project

We are looking for an eye catching, unique business card design that incorporates our logo and a photo of the mortgage associate.

We will need to have our business address included (could be on the back of the card), as well as the mortgage associate's information:

Name
Position
Phone
Email

Logo attached.

Target Market(s)

Clients (people purchasing homes, renewing existing mortgages, or refinancing existing mortgages)
Referral sources such as realtors, financial advisors, relocation specialists, real estate lawyers...

Industry/Entity Type

Business

Requirements
Must have
• Logo
Name and contact information of associate
Address of brokerage
Nice to have
• Photo of the agent

```html
<!DOCTYPE html>
<html lang="en">
<head>
<meta charset="utf-8">
<title>Keystone Lending Group – Business Card</title>
<link rel="stylesheet" href="https://fonts.googleapis.com/css2?family=Open+Sans:wght@400;600;700;800&display=swap">
<style>
  :root {
    --backdrop: #c9c9c9;
    --card-white: #ffffff;
    --charcoal-deep: #1d1e20;
    --charcoal-light: #3a3b3e;
    --brand-red: #b3151b;
    --brand-red-dark: #8c0f14;
    --ink: #2e2f31;
    --text-light: #f2f2f2;
    --text-muted: #8d8f93;
    --photo-suit: #2a2d33;
    --photo-light: #d9dde2;
  }
  * { box-sizing: border-box; margin: 0; padding: 0; }
  html, body {
    width: 1200px; height: 900px; overflow: hidden;
    background: var(--backdrop);
    font-family: "Open Sans", Arial, sans-serif;
  }
  .stage { position: relative; width: 1200px; height: 900px; }
  .card {
    position: absolute; top: 296px;
    width: 540px; height: 308px;
    border-radius: 18px; overflow: hidden;
    box-shadow: 0 14px 30px rgba(0,0,0,0.28);
  }
  .card--front { left: 40px; background: var(--card-white); }
  .card--back {
    left: 620px;
    background: radial-gradient(ellipse at 50% 40%, var(--charcoal-light), var(--charcoal-deep) 80%);
  }

  /* front */
  .front-brand {
    position: absolute; left: 26px; top: 62px;
    display: flex; align-items: center; gap: 10px;
  }
  .brand-square { width: 20px; height: 20px; background: var(--brand-red); flex: none; }
  .brand-name {
    font-weight: 800; font-size: 27px; line-height: 1.05;
    color: var(--ink); letter-spacing: 0.2px;
  }
  .associate-photo {
    position: absolute; left: 360px; top: 12px;
    width: 140px; height: 154px;
    background: linear-gradient(180deg, var(--photo-light) 0%, #b9bec6 40%, var(--photo-suit) 62%, var(--photo-suit) 100%);
    border-radius: 4px 4px 0 0;
  }
  .front-lower {
    position: absolute; left: 0; top: 160px; width: 100%; bottom: 0;
    background: linear-gradient(180deg, var(--charcoal-light), var(--charcoal-deep));
  }
  .tagline-band {
    position: absolute; left: 0; top: 150px;
    width: 100%; height: 22px;
    background: linear-gradient(90deg, var(--brand-red-dark), var(--brand-red) 60%, var(--brand-red-dark));
    color: var(--text-light);
    font-size: 12px; letter-spacing: 3.1px;
    line-height: 22px; padding-left: 26px; white-space: nowrap;
  }
  .associate-name {
    position: absolute; left: 24px; top: 184px;
    font-weight: 700; font-size: 17px; color: var(--text-light);
  }
  .associate-role {
    position: absolute; left: 24px; top: 207px;
    font-size: 12px; color: var(--brand-red);
  }
  .contact-list {
    position: absolute; left: 22px; top: 240px;
    list-style: none;
  }
  .contact-item {
    display: flex; align-items: center; gap: 7px;
    font-size: 14px; color: var(--text-light); line-height: 22px;
  }
  .contact-icon { width: 12px; height: 12px; flex: none; }

  /* back */
  .back-brand {
    position: absolute; left: 0; top: 100px; width: 100%;
    display: flex; justify-content: center; align-items: center; gap: 12px;
  }
  .back-brand .brand-name { color: var(--text-light); font-size: 28px; }
  .back-tagline {
    position: absolute; left: 0; top: 172px; width: 100%;
    text-align: center; font-size: 11px; letter-spacing: 1px;
    color: var(--text-muted);
  }
  .back-address {
    position: absolute; left: 0; top: 252px; width: 100%;
    text-align: center; font-size: 14px; font-weight: 600;
    color: var(--text-light);
  }
</style>
</head>
<body>
<main class="stage">
  <section class="card card--front">
    <div class="front-brand">
      <span class="brand-square"></span>
      <span class="brand-name">KEYSTONE<br>LENDING GROUP</span>
    </div>
    <div class="associate-photo" role="img" aria-label="Portrait photo of the mortgage associate in a dark suit"></div>
    <div class="front-lower"></div>
    <div class="tagline-band">Home loans built around the way you live</div>
    <h1 class="associate-name">DANIEL REYES</h1>
    <p class="associate-role">mortgage associate</p>
    <ul class="contact-list">
      <li class="contact-item">
        <svg class="contact-icon" viewBox="0 0 24 24"><path fill="#b3151b" d="M6.6 10.8a15.1 15.1 0 0 0 6.6 6.6l2.2-2.2a1 1 0 0 1 1-.25 11.4 11.4 0 0 0 3.6.57 1 1 0 0 1 1 1V20a1 1 0 0 1-1 1A17 17 0 0 1 3 4a1 1 0 0 1 1-1h3.5a1 1 0 0 1 1 1c0 1.25.2 2.45.57 3.57a1 1 0 0 1-.25 1z"/></svg>
        (555)410-2837
      </li>
      <li class="contact-item">
        <svg class="contact-icon" viewBox="0 0 24 24"><rect x="2" y="5" width="20" height="14" rx="2" fill="#b3151b"/><path d="M3 6l9 7 9-7" fill="none" stroke="#2b2c2e" stroke-width="2"/></svg>
        daniel@keystonelending.com
      </li>
    </ul>
  </section>

  <section class="card card--back">
    <div class="back-brand">
      <span class="brand-square"></span>
      <span class="brand-name">KEYSTONE LENDING GROUP</span>
    </div>
    <p class="back-tagline">Home loans built around the way you live</p>
    <p class="back-address">Po Box: 40215, Alder Street, Springfield</p>
  </section>
</main>
</body>
</html>
```